Urgent - brand new business card for a startup technical advisory and incubation business in Sydney

We need a brand new business card design for BrightForge. We are a startup technical advisory and incubation business based in Sydney Australia. We work with entrepreneurs and innovators to help rapidly and efficiently turn their ideas into reality and to ensure they have the technical platform required for growth.

Our name is partly inspired by our love of lean product development methods and the lean startup movement.

We would like clean, uncluttered designs that feature our two logo colours and communicate a professional but creative, in-touch and entrepreneurial business.

PLEASE SEE MUST HAVE PRIORITIES FOR DRAFT CONTACT INFORMATION AND OTHER DESIRED TEXT ON CARD.
Updates

We have now updated the brief to include draft business card contact information and also some additional desired text to feature on the card design.    Please review the Must Have priorities.

Also final updated source files for the horizontal and vertical versions have now been uploaded and should be used for any designs.

Thanks!

Target Market(s)

Entrepeneurs, innovators, startup investors looking for a strong product development partner

Industry/Entity Type

Business

Requirements
Must have
• Feature our two logo colours
Be a relatively clean, pared back overall design - quite minimalist

Updated source files (AI) for vertical and horizontal layouts attached.

Draft contact information for business card:
Tom Harcourt
Founder & CTO
Phone: +61 427 555123
Email: xxxx@brightforge.example
Callwire: xxxxxharcourt
Chirper: tharcourt

www.brightforge.example

We would also like the overall design to include the phrase "You have great ideas. Let us make them happen." (probably in a reasonably subtle way)

Nice to have
• Inspire me! Double-sided designs are fine with logo, phrase, (URL?) on one side and contact details on other (+ any other design elements)

Logo on business card can be either with lightbulb above the wording as per example here or to the left of the BrightForge wording - both layouts in files provided.
Should not have
• Shouldn't look like a Pendrel Suite business card template :-)

```html
<!DOCTYPE html>
<html lang="en">
<head>
<meta charset="utf-8">
<title>BrightForge business card</title>
<link rel="stylesheet" href="https://fonts.googleapis.com/css2?family=Source+Sans+3:wght@400;600&display=swap">
<style>
  :root {
    --brand-cyan: #00b4ef;
    --ink: #3c3c3c;
    --ink-dark: #1e1e1e;
    --rule: #6a6a6a;
    --card: #ffffff;
    --backdrop: #3b2217;
  }
  * { margin: 0; padding: 0; box-sizing: border-box; }
  html, body { width: 1200px; height: 836px; overflow: hidden; }
  body {
    background: var(--backdrop);
    font-family: "Source Sans 3", Arial, sans-serif;
    color: var(--ink);
  }
  .stage { position: relative; width: 1200px; height: 836px; }

  .card {
    position: absolute;
    width: 464px;
    height: 265px;
    background: var(--card);
    overflow: hidden;
  }
  .card--front { left: 361px; top: 99px; }
  .card--back-light { left: 120px; top: 430px; }
  .card--back-brand { left: 612px; top: 431px; background: var(--brand-cyan); }

  /* Front: contact block */
  .contact-col {
    position: absolute;
    list-style: none;
    font-size: 11px;
    line-height: 18px;
  }
  .contact-col li { display: flex; align-items: center; gap: 5px; white-space: nowrap; }
  .contact-col svg { width: 11px; height: 11px; flex: none; }
  .contact-col--primary { left: 22px; top: 55px; }
  .contact-col--social { left: 183px; top: 64px; line-height: 19px; }

  .divider {
    position: absolute;
    width: 1px;
    height: 50px;
    background: var(--rule);
  }
  .divider--one { left: 172px; top: 58px; }
  .divider--two { left: 330px; top: 58px; }

  .identity { position: absolute; left: 341px; top: 63px; white-space: nowrap; }
  .identity__name {
    color: var(--brand-cyan);
    font-size: 15px;
    font-weight: 400;
    text-transform: uppercase;
    line-height: 19px;
  }
  .identity__role { font-size: 11px; margin-top: 3px; }

  /* Brand name lockup */
  .brand {
    position: absolute;
    display: flex;
    align-items: center;
    gap: 8px;
    font-weight: 600;
    white-space: nowrap;
  }
  .brand__dot { border-radius: 50%; background: var(--brand-cyan); flex: none; }
  .card--front .brand {
    left: 50%; top: 178px; transform: translateX(-50%);
    font-size: 27px; color: var(--ink-dark);
  }
  .card--front .brand__dot { width: 30px; height: 30px; }

  .brand--large {
    left: 50%; top: 50%; transform: translate(-50%, -50%);
    font-size: 31px;
    gap: 10px;
  }
  .card--back-light .brand--large { color: var(--ink-dark); }
  .brand--large .brand__dot { width: 40px; height: 40px; }
  .card--back-brand .brand--large { color: #ffffff; }
  .card--back-brand .brand__dot { background: #ffffff; }
</style>
</head>
<body>
<main class="stage">

  <section class="card card--front" aria-label="Business card front">
    <ul class="contact-col contact-col--primary">
      <li>
        <svg viewBox="0 0 12 12" aria-hidden="true"><circle cx="6" cy="6" r="6" fill="var(--brand-cyan)"/><path d="M4 3.2c.4-.3.8-.3 1 .1l.5.9c.2.3 0 .6-.2.8-.2.2-.1.5.2.9.4.5.7.6.9.4.2-.2.5-.3.8-.1l.8.5c.3.2.3.6 0 .9-.8.8-2.3.2-3.4-1.2C3.6 5.1 3.4 3.8 4 3.2z" fill="#fff"/></svg>
        +61 427 555123
      </li>
      <li>
        <svg viewBox="0 0 12 12" aria-hidden="true"><rect x="0.5" y="2.5" width="11" height="7.5" fill="var(--brand-cyan)"/><path d="M1 3l5 3.6L11 3" stroke="#fff" stroke-width="1" fill="none"/></svg>
        xxxx@brightforge.example
      </li>
      <li>
        <svg viewBox="0 0 12 12" aria-hidden="true"><g fill="none" stroke="var(--brand-cyan)" stroke-width="1"><circle cx="6" cy="6" r="5.2"/><ellipse cx="6" cy="6" rx="2.2" ry="5.2"/><path d="M0.8 6h10.4M1.8 3.3h8.4M1.8 8.7h8.4"/></g></svg>
        www.brightforge.example
      </li>
    </ul>

    <span class="divider divider--one"></span>

    <ul class="contact-col contact-col--social">
      <li>
        <svg viewBox="0 0 12 12" aria-hidden="true"><rect x="0.5" y="0.5" width="11" height="11" rx="2" fill="var(--brand-cyan)"/></svg>
        Callwire: xxxxxharcourt
      </li>
      <li>
        <svg viewBox="0 0 12 12" aria-hidden="true"><rect x="0.5" y="0.5" width="11" height="11" rx="2" fill="var(--brand-cyan)"/></svg>
        Chirper: tharcourt
      </li>
    </ul>

    <span class="divider divider--two"></span>

    <div class="identity">
      <p class="identity__name">Tom Harcourt</p>
      <p class="identity__role">Founder &amp; CTO</p>
    </div>

    <div class="brand">
      <span class="brand__dot" aria-hidden="true"></span>
      <span class="brand__name">BrightForge</span>
    </div>
  </section>

  <section class="card card--back-light" aria-label="Business card back, white">
    <div class="brand brand--large">
      <span class="brand__dot" aria-hidden="true"></span>
      <span class="brand__name">BrightForge</span>
    </div>
  </section>

  <section class="card card--back-brand" aria-label="Business card back, brand colour">
    <div class="brand brand--large">
      <span class="brand__dot" aria-hidden="true"></span>
      <span class="brand__name">BrightForge</span>
    </div>
  </section>

</main>
</body>
</html>
```